Cloud Hosting Provider Web Site

We need to create the design for Nimbo-Pails.net a new Cloud Hosting Provider Website.

We already have a logo and a draft website with preliminary content showing the desired structure for the final web site.

I need a design for the Home Page and all 10 Internal web pages currently linked from the draft home page.

The documentation site (/docs) Customer Portal (/portal) and Support site (/support) are not part of this design project.

We need images to illustrate all pages which of course need to be consistent with the content. Please read carefully the text of each page in the draft web site to understand the purpose of each page and illustrate it accordingly.

All pages must be illustrated with images, I do not want any single page with just text.

I want to maintain the slides idea of the draft website home page.

The web site must look professional, we are competitors of huge companies like tallow grid systems (tgs.tallowgrid.com), Velquist Oriel (oriel.velquist.com) and DuneLoft (www.duneloft.com) so we need to look as serious as them.

You may download the draft web site pages to style them, I need fully finalized HTML / CSS and image files.

A top link bar and link footer must be included in every page.

Also the web site will have the possibility to start a chat conversation with a sales agent, so a graphical link to do so must be included in the design, together with a chat window design (including HTML/CSS)

Information for accessing the draft web site follows:

URL: www.nimbo-pails.net
username: design
password: QOPqop987654

If you need any additional information please let me know.

```html
<!DOCTYPE html>
<html lang="en">
<head>
<meta charset="utf-8">
<title>Nimbo-Pails.net — Private Cloud Hosting</title>
<link rel="stylesheet" href="https://fonts.googleapis.com/css2?family=Roboto+Condensed:wght@400;700&family=PT+Sans+Narrow:wght@700&family=Open+Sans:wght@400;600;700&display=swap">
<style>
  :root {
    --frame: #e6e6e6;
    --navy: #15124a;
    --navy-deep: #0c1250;
    --brand-blue: #1b6fb5;
    --sky: #2a9fd8;
    --logo-ink: #1b3563;
    --white: #ffffff;
    --footer-top: #d9d9d9;
    --footer-bottom: #f2f2f2;
    --footer-text: #3c3c3c;
    --heading-blue: #2285c9;
    --field: #d3d3d3;
  }
  * { box-sizing: border-box; margin: 0; padding: 0; }
  html, body { width: 873px; height: 1200px; overflow: hidden; }
  body { background: var(--frame); font-family: "Open Sans", sans-serif; position: relative; }
  a { text-decoration: none; }

  .page { position: absolute; left: 11px; top: 10px; width: 851px; height: 1180px; background: var(--white); overflow: hidden; }

  /* Hero */
  .hero { position: absolute; left: 0; top: 0; width: 851px; height: 474px; }
  .hero-photo { position: absolute; inset: 0;
    background:
      radial-gradient(ellipse 230px 330px at 440px 330px, rgba(40,44,56,0.85), rgba(60,70,90,0.35) 60%, rgba(255,255,255,0) 100%),
      linear-gradient(180deg, #eef5fb 0%, #cfe3f3 55%, #a9cbe8 100%); }
  .brand { position: absolute; left: 14px; top: 82px; display: flex; align-items: center; gap: 6px; }
  .brand-dot { width: 16px; height: 16px; border-radius: 50%; background: var(--brand-blue); }
  .brand-name { font-family: "Open Sans", sans-serif; font-weight: 700; font-size: 19px; color: var(--logo-ink); letter-spacing: -0.2px; }

  .chat-link { position: absolute; left: 676px; top: 8px; width: 172px; height: 48px; }
  .chat-pill { position: absolute; left: 38px; top: 8px; width: 134px; height: 36px; border-radius: 4px 8px 8px 4px;
    background: linear-gradient(180deg, #1a8fd0, #0f6fb0); box-shadow: 0 1px 3px rgba(0,0,0,0.3); }
  .chat-title { position: absolute; left: 0; right: 0; top: 3px; text-align: center; font-family: "Roboto Condensed", sans-serif; font-weight: 700; font-size: 12.5px; color: var(--white); padding-left: 10px; }
  .chat-sub { position: absolute; left: 46px; top: 20px; width: 96px; height: 14px; border-radius: 7px; background: #29b1e8; text-align: center;
    font-family: "Open Sans", sans-serif; font-weight: 700; font-size: 8.5px; line-height: 14px; color: var(--navy-deep); }
  .chat-agent { position: absolute; left: 0; top: 0; width: 46px; height: 46px; border-radius: 50%; border: 2px solid var(--white);
    background: radial-gradient(circle at 50% 40%, #e7c8b0, #7b6a60); box-shadow: 0 1px 3px rgba(0,0,0,0.35); }

  .main-nav { position: absolute; left: 349px; top: 80px; width: 488px; height: 22px; border-radius: 5px;
    background: linear-gradient(180deg, #1a2a80, var(--navy-deep)); display: flex; align-items: center; justify-content: center; }
  .main-nav a { font-family: "Roboto Condensed", sans-serif; font-weight: 700; font-size: 10px; color: var(--white); }
  .main-nav .sep { color: var(--white); font-size: 9px; margin: 0 11px; font-family: "Roboto Condensed", sans-serif; }

  .hero-copy { position: absolute; left: 0; width: 851px; text-align: center; font-family: "PT Sans Narrow", sans-serif; font-weight: 700; color: var(--white);
    text-shadow: 0 0 2px #000, 1px 1px 2px #000, -1px -1px 2px #000; }
  .hero-copy.headline { top: 328px; font-size: 41px; letter-spacing: -0.5px; }
  .hero-copy.subline { top: 372px; font-size: 30px; letter-spacing: -0.4px; }

  /* Services grid */
  .services { position: absolute; left: 0; top: 474px; width: 851px; height: 447px;
    background: radial-gradient(ellipse 200px 160px at 425px 40px, #1a8ad6 0%, #124a9a 45%, var(--navy) 100%); }
  .service { position: absolute; width: 260px; text-align: center; }
  .service .icon { position: absolute; left: 102px; top: -32px; width: 56px; height: 56px; border-radius: 50%; background: #07071c;
    border: 2px solid var(--white); box-shadow: 0 0 0 1px #07071c; display: flex; align-items: center; justify-content: center; }
  .service h2 { position: absolute; left: 0; right: 0; top: 32px; font-family: "Roboto Condensed", sans-serif; font-weight: 400; font-size: 15px; line-height: 16px; color: var(--white); text-transform: uppercase; }
  .service .read-more { position: absolute; left: 91px; top: 74px; width: 78px; height: 21px; border: 1.5px solid var(--white); border-radius: 2px;
    font-size: 10.5px; line-height: 18px; color: var(--white); }
  .service.one-line h2 { top: 22px; }
  .service.one-line .read-more { top: 58px; }
  .service h2.keep-case { text-transform: none; }

  /* Footer */
  .site-footer { position: absolute; left: 0; top: 921px; width: 851px; height: 232px;
    background: linear-gradient(180deg, var(--footer-top), var(--footer-bottom)); border-top: 4px solid var(--white); }
  .site-footer h3 { position: absolute; font-size: 10.5px; font-weight: 700; color: var(--heading-blue); }
  .about-text { position: absolute; left: 36px; top: 58px; width: 180px; font-size: 8.8px; line-height: 13.7px; color: var(--footer-text); }
  .footer-nav { position: absolute; left: 248px; top: 57px; list-style: none; }
  .footer-nav li { font-size: 8.8px; line-height: 15.2px; color: var(--footer-text); }
  .field { position: absolute; left: 377px; width: 160px; height: 18px; background: var(--field); font-size: 9px; font-weight: 700; color: #333; padding: 3px 6px; }
  .field.message { height: 46px; }
  .send { position: absolute; left: 377px; top: 176px; width: 76px; height: 28px; background: #0e0e0e; border: 1px solid #555; box-shadow: 0 1px 2px rgba(0,0,0,0.4);
    color: var(--white); font-size: 11px; font-weight: 700; text-align: center; line-height: 26px; }
  .contact-row { position: absolute; left: 578px; display: flex; align-items: flex-start; gap: 7px; font-size: 8.8px; line-height: 10.5px; color: var(--footer-text); }
  .contact-row svg { flex: none; margin-top: 1px; }
  .social { position: absolute; left: 594px; top: 138px; display: flex; gap: 5px; }
  .social span { width: 16px; height: 16px; border-radius: 50%; background: var(--sky); }
  .footer-brand { position: absolute; left: 726px; top: 110px; display: flex; align-items: center; gap: 4px; }
  .footer-brand .brand-dot { width: 11px; height: 11px; }
  .footer-brand .brand-name { font-size: 11.5px; }

  .copyright { position: absolute; left: 0; top: 1153px; width: 851px; height: 27px; background: var(--white); box-shadow: 0 -6px 8px -6px rgba(0,0,0,0.35);
    text-align: center; font-size: 7.5px; line-height: 27px; color: #333; }
</style>
</head>
<body>
<div class="page">

  <header class="hero">
    <div class="hero-photo" role="img" aria-label="Businessman in a suit holding a tablet, with floating cloud, download, upload and globe panels around him"></div>

    <a class="brand" href="#">
      <span class="brand-dot"></span>
      <span class="brand-name">Nimbo-Pails.net</span>
    </a>

    <a class="chat-link" href="#">
      <span class="chat-pill">
        <span class="chat-title">QUESTIONS?</span>
        <span class="chat-sub">CHAT WITH US</span>
      </span>
      <span class="chat-agent" role="img" aria-label="Sales agent with headset"></span>
    </a>

    <nav class="main-nav">
      <a href="#">OUR COMPANY</a><span class="sep">I</span>
      <a href="#">USE CASES</a><span class="sep">I</span>
      <a href="#">CLOUD SERVICES</a><span class="sep">I</span>
      <a href="#">PAIL'S INFRASTRUCTURE</a><span class="sep">I</span>
      <a href="#">CUSTOMER LOGIN</a>
    </nav>

    <p class="hero-copy headline">Create your own private cloud, pail by pail.</p>
    <p class="hero-copy subline">Each PAIL just $ 990 per month!</p>
  </header>

  <section class="services">
    <div class="service" style="left:23px; top:12px;">
      <span class="icon"><svg width="30" height="22" viewBox="0 0 30 22"><path d="M8 19h15a6 6 0 0 0 0-12 8 8 0 0 0-15-1A6 6 0 0 0 8 19z" fill="none" stroke="#fff" stroke-width="2.2"/></svg></span>
      <h2>Become a cloud<br>hosting provider</h2>
      <a class="read-more" href="#">Read More</a>
    </div>
    <div class="service" style="left:306px; top:12px;">
      <span class="icon"><svg width="30" height="24" viewBox="0 0 30 24"><g fill="#fff"><rect x="3" y="4" width="6" height="18"/><rect x="12" y="1" width="6" height="21"/><rect x="21" y="4" width="6" height="18"/></g><g stroke="#07071c" stroke-width="1"><path d="M4 9h4M4 13h4M13 7h4M13 11h4M13 15h4M22 9h4M22 13h4"/></g></svg></span>
      <h2>Virtualize your server<br>infrastructure</h2>
      <a class="read-more" href="#">Read More</a>
    </div>
    <div class="service" style="left:590px; top:12px;">
      <span class="icon"><svg width="30" height="26" viewBox="0 0 30 26"><path d="M7 16h16a5.5 5.5 0 0 0 0-11 7.5 7.5 0 0 0-14-1A5.5 5.5 0 0 0 7 16z" fill="#fff"/><g fill="#07071c"><rect x="10" y="7" width="10" height="2.4"/><rect x="10" y="10.5" width="10" height="2.4"/></g><path d="M15 16v5M9 23h12" stroke="#fff" stroke-width="1.8"/></svg></span>
      <h2>Move from public to<br>private cloud</h2>
      <a class="read-more" href="#">Read More</a>
    </div>

    <div class="service" style="left:23px; top:176px;">
      <span class="icon"><svg width="30" height="24" viewBox="0 0 30 24"><path d="M7 20h16a6 6 0 0 0 0-12 8 8 0 0 0-15-1A6 6 0 0 0 7 20z" fill="#fff"/><rect x="9" y="10" width="12" height="7" fill="none" stroke="#07071c" stroke-width="1.4"/><path d="M7 19h16" stroke="#07071c" stroke-width="1.4"/></svg></span>
      <h2>Saving money with<br>the private cloud</h2>
      <a class="read-more" href="#">Read More</a>
    </div>
    <div class="service" style="left:306px; top:176px;">
      <span class="icon"><svg width="30" height="26" viewBox="0 0 30 26"><path d="M7 18h16a6 6 0 0 0 0-12 8 8 0 0 0-15-1A6 6 0 0 0 7 18z" fill="#fff"/><circle cx="14" cy="12" r="4" fill="none" stroke="#07071c" stroke-width="1.8"/><path d="M17 15l6 6" stroke="#fff" stroke-width="3"/><path d="M17 15l2.5 2.5" stroke="#07071c" stroke-width="1.8"/></svg></span>
      <h2>Nimbo-Pails<br>technical features</h2>
      <a class="read-more" href="#">Read More</a>
    </div>
    <div class="service" style="left:590px; top:176px;">
      <span class="icon"><svg width="30" height="24" viewBox="0 0 30 24"><path d="M7 20h16a6 6 0 0 0 0-12 8 8 0 0 0-15-1A6 6 0 0 0 7 20z" fill="#fff"/><rect x="10" y="9" width="10" height="9" fill="none" stroke="#07071c" stroke-width="1.3"/><path d="M12 12h6M12 14.5h6" stroke="#07071c" stroke-width="1"/></svg></span>
      <h2>Nimbo-Pails virtual data<br>center menagement platform</h2>
      <a class="read-more" href="#">Read More</a>
    </div>

    <div class="service one-line" style="left:23px; top:340px;">
      <span class="icon"><svg width="30" height="24" viewBox="0 0 30 24"><path d="M7 20h16a6 6 0 0 0 0-12 8 8 0 0 0-15-1A6 6 0 0 0 7 20z" fill="#fff"/><path d="M15 9l1.7 3.6 3.8.4-2.8 2.6.8 3.8-3.5-2-3.5 2 .8-3.8-2.8-2.6 3.8-.4z" fill="#07071c"/></svg></span>
      <h2>Cloud services</h2>
      <a class="read-more" href="#">Read More</a>
    </div>
    <div class="service one-line" style="left:306px; top:340px;">
      <span class="icon"><svg width="30" height="24" viewBox="0 0 30 24"><path d="M7 20h16a6 6 0 0 0 0-12 8 8 0 0 0-15-1A6 6 0 0 0 7 20z" fill="#fff"/><g fill="#07071c"><circle cx="15" cy="12" r="2.2"/><circle cx="10.5" cy="13.5" r="1.8"/><circle cx="19.5" cy="13.5" r="1.8"/><path d="M11.5 19a3.5 3.5 0 0 1 7 0z"/><path d="M7.5 19a3 3 0 0 1 5.5-1.5V19z"/><path d="M22.5 19a3 3 0 0 0-5.5-1.5V19z"/></g></svg></span>
      <h2 class="keep-case">7x24x365 SUPPORT</h2>
      <a class="read-more" href="#">Read More</a>
    </div>
    <div class="service one-line" style="left:590px; top:340px;">
      <span class="icon"><svg width="30" height="24" viewBox="0 0 30 24"><path d="M7 20h16a6 6 0 0 0 0-12 8 8 0 0 0-15-1A6 6 0 0 0 7 20z" fill="#fff"/><path d="M11 13h2.5v6H11zM14.5 19v-6l2-3.5c1 0 1.5.6 1.2 2l-.4 1.5h3c.8 0 1.2.7 1 1.4l-1 3.6c-.2.6-.6 1-1.2 1z" fill="#07071c"/></svg></span>
      <h2>Pricing</h2>
      <a class="read-more" href="#">Read More</a>
    </div>
  </section>

  <footer class="site-footer">
    <h3 style="left:36px; top:34px;">About Nimbo-Pails.net</h3>
    <p class="about-text">Lorem ipsum dolor sit amet, consectetue adipiscing elit, sed diam nonummy nibh euismod tincidunt ut laoreet dolore mag aliquam erat volutpat. Ut wisi enim admi veniam, quis nostrud exerci tation ullam corper suscipit lobortis nisl ut aliquip ex ea commodo consequat. Duis autem vel eum iriure dolor in hendrerit in vulputa velit esse molestie consequat.</p>

    <h3 style="left:248px; top:34px;">Navigation</h3>
    <ul class="footer-nav">
      <li>Our Company</li>
      <li>Use Cases</li>
      <li>Cloud Services</li>
      <li>Pail's Infrastructure</li>
      <li>Customer Login</li>
    </ul>

    <h3 style="left:377px; top:34px;">Quick Contact</h3>
    <div class="field" style="top:56px;">Name</div>
    <div class="field" style="top:80px;">Email</div>
    <div class="field" style="top:104px;">Phone</div>
    <div class="field message" style="top:128px;">Message</div>
    <div class="send">SEND</div>

    <h3 style="left:578px; top:34px;">Contact Info</h3>
    <div class="contact-row" style="top:60px;">
      <svg width="9" height="12" viewBox="0 0 9 12"><path d="M4.5 0A4.5 4.5 0 0 0 0 4.5C0 8 4.5 12 4.5 12S9 8 9 4.5A4.5 4.5 0 0 0 4.5 0z" fill="#333"/><circle cx="4.5" cy="4.5" r="1.7" fill="#e0e0e0"/></svg>
      <span>Lorem Ipsum<br>New York NY</span>
    </div>
    <div class="contact-row" style="top:88px;">
      <svg width="10" height="9" viewBox="0 0 10 9"><path d="M0 3c0-2 2-3 5-3s5 1 5 3H7.5V2h-5v1zM2 4h6l1.5 5h-9z" fill="#333"/></svg>
      <span>123.456.7890</span>
    </div>
    <div class="contact-row" style="top:109px;">
      <svg width="10" height="8" viewBox="0 0 10 8"><rect width="10" height="8" fill="#333"/><path d="M0 0l5 4.5L10 0" fill="none" stroke="#e0e0e0" stroke-width="1"/></svg>
      <span>info@nimbo-pails.net</span>
    </div>
    <div class="social"><span></span><span></span><span></span></div>

    <div class="footer-brand">
      <span class="brand-dot"></span>
      <span class="brand-name">Nimbo-Pails.net</span>
    </div>
  </footer>

  <div class="copyright">COPYRIGHT © 2015 NIMBO-PAILS.NET.&nbsp; ALL RIGHTS RESERVED.</div>
</div>
</body>
</html>
```